Rural contractor needs professional informative business card

We need a business card design that looks professional but also includes information about the services that the business offers.
The business is an earthmoving and transport business. All of the services offered are listed on the old card attached.
The business is aimed at farmers so the design we are after is a classic look. The card needs to include all of the information that is listed on the old card design uploaded as an attachment. We recognize that this is a lot of information to fit on a business card but it also operates as a key marketing tool so is very important to the business.
Feel free to send me your questions.
Thanks
Reason: We are having trouble deciding between all these great designs - thank you for your efforts
We would love to see some designs using red with a little white and black. Also feel free to re-design our logo if you feel it needs to be to fit your designs. Thank you

```html
<!DOCTYPE html>
<html lang="en">
<head>
<meta charset="utf-8">
<title>RB Hartley Contracting – Business Card</title>
<link rel="stylesheet" href="https://fonts.googleapis.com/css2?family=Lato:wght@400;700&display=swap">
<style>
  :root {
    --page-bg: #e9e6e1;
    --card-white: #ffffff;
    --card-black: #141414;
    --ink: #222222;
    --ink-soft: #444444;
    --accent-blue: #3a6fc4;
    --sky-top: #4f86d6;
    --sky-low: #b9d0ea;
    --dusk-top: #d9dde6;
    --dusk-low: #e8d7cf;
    --ground: #a08a70;
    --ground-dark: #6b5a49;
    --white: #ffffff;
  }
  * { box-sizing: border-box; margin: 0; padding: 0; }
  html, body { width: 1200px; height: 913px; overflow: hidden; }
  body {
    background: var(--page-bg);
    font-family: 'Lato', Arial, sans-serif;
    position: relative;
  }
  .card {
    position: absolute;
    width: 540px;
    height: 310px;
    border-radius: 22px;
    overflow: hidden;
    box-shadow: 0 6px 18px rgba(0,0,0,.18);
  }

  /* Front */
  .card-front { left: 40px; top: 300px; background: var(--card-white); }
  .front-photo {
    position: absolute; left: 262px; top: 22px; width: 256px; height: 186px;
    background: linear-gradient(180deg, var(--sky-top) 0%, var(--sky-low) 52%, var(--ground) 60%, var(--ground-dark) 100%);
    border: 1px solid #8a8a8a;
  }
  .front-tagline {
    position: absolute; left: 262px; top: 218px; width: 256px;
    text-align: center; color: var(--accent-blue); font-size: 13px; font-weight: 700;
  }
  .brand-name {
    position: absolute; left: 30px; top: 78px; width: 210px;
    font-size: 22px; font-weight: 700; color: var(--ink); line-height: 1.15;
  }
  .contact-block {
    position: absolute; right: 300px; top: 150px; text-align: right; color: var(--ink-soft);
  }
  .person-name { color: var(--accent-blue); font-size: 18px; font-weight: 700; }
  .person-role { font-size: 12px; margin-bottom: 14px; }
  .contact-line { font-size: 12px; line-height: 1.55; display: flex; justify-content: flex-end; align-items: center; gap: 5px; }
  .contact-line svg { width: 11px; height: 11px; fill: var(--accent-blue); }

  /* Back */
  .card-back { left: 620px; top: 300px; background: linear-gradient(160deg, #2a2a2a, var(--card-black) 60%); }
  .back-brand {
    position: absolute; left: 22px; top: 22px; color: var(--white); font-size: 12px; font-weight: 700;
  }
  .back-photo {
    position: absolute; left: 108px; top: -70px; width: 560px; height: 460px; border-radius: 50%;
    border: 3px solid var(--white);
    background: linear-gradient(180deg, var(--dusk-top) 0%, var(--dusk-low) 38%, #8d7c6b 48%, #5a4c40 75%, #2c2622 100%);
  }
  .back-title {
    position: absolute; left: 150px; top: 42px; font-size: 15px; letter-spacing: .5px; color: #2a2a2a;
  }
  .service-group { position: absolute; color: var(--white); }
  .service-group h2 { font-size: 15px; font-weight: 700; margin-bottom: 2px; }
  .service-group ul { list-style: none; font-size: 11.5px; line-height: 1.35; }
  .service-transport { right: 22px; top: 100px; text-align: right; }
  .service-transport li::after { content: " •"; }
  .service-earthmoving { left: 150px; top: 196px; }
  .service-earthmoving li::before { content: "• "; }
</style>
</head>
<body>
  <section class="card card-front" aria-label="Card front">
    <div class="brand-name">RB Hartley Contracting</div>
    <div class="contact-block">
      <div class="person-name">Tom Hartley</div>
      <div class="person-role">Business Person</div>
      <div class="contact-line">27 Kestrel Street</div>
      <div class="contact-line">Dunmore 2830</div>
      <div class="contact-line">0400 555 182
        <svg viewBox="0 0 10 10"><rect x="2" y="0" width="6" height="10" rx="1"/></svg></div>
      <div class="contact-line">tom.hartley@mailbox.example
        <svg viewBox="0 0 10 8"><path d="M0 0h10v8H0z M0 0l5 4 5-4" stroke="#fff" stroke-width=".8"/></svg></div>
    </div>
    <div class="front-photo" role="img" aria-label="Photo of a white prime mover truck parked on a gravel yard under a blue sky"></div>
    <div class="front-tagline">Earthmoving &amp; Transport Solutions</div>
  </section>

  <section class="card card-back" aria-label="Card back">
    <div class="back-photo" role="img" aria-label="Photo of a truck hauling cotton bales on a dirt road at dusk"></div>
    <div class="back-brand">RB Hartley Contracting</div>
    <div class="back-title">EARTHMOVING &amp; TRANSPORT SOLUTIONS</div>
    <div class="service-group service-transport">
      <h2>Transport</h2>
      <ul><li>Grain</li><li>Cotton</li><li>Sand &amp; Gravel</li><li>Wool</li></ul>
    </div>
    <div class="service-group service-earthmoving">
      <h2>Earthmoving</h2>
      <ul><li>Road Building &amp; Maintence</li><li>Poly Pipe laying</li><li>Clearing fence lines</li><li>Sand &amp; Gravel Supplies</li></ul>
    </div>
  </section>
</body>
</html>
```